Stationary Design For Youthful Disability Company

Hi Designers,
Looking to have our brand applied to a range of stationary items to professionalise our approach, we are a disability services company that aligns young carers with disabled youth and adults. Our stationary needs to look professional but can verge into a fun bright territory too.
Winning designer will be first contact for advertising campaign, form creation and web-design in January 2014.
Cheers,
Tom
Brightpath Disability Services
Design Briefs
Stationary.
Sleek fun and bright stationary that portrays a professional but youthful disability service. Company prides its self on delivering youthful carers to disabled clients.
Needed:
- Business Card - Letter Head - Email Signature
- Invoice / Quotation (blank branded paper) - Normal Envelope - A4 Envelope
- Stationary for future forms or documents. (Doesn't need to include all contacts, branding is enough).
Would be nice if we were able to edit numbers etc as we change them.
Include:
Lachlan Corrigan - Managing Director
M. 0478 295 604
E. lcorrigan@brightpathdisability.example
A. PO Box 87 Wexcombe 3391
ABN. 47392015863

```html
<!DOCTYPE html>
<html lang="en">
<head>
<meta charset="utf-8">
<title>Brightpath Disability Services – Stationery</title>
<link href="https://fonts.googleapis.com/css2?family=Open+Sans:wght@400;600;700&display=swap" rel="stylesheet">
<style>
:root{
  --stage:#e0e0e0;
  --paper:#f4f4f4;
  --ink:#7a7a7a;
  --ink-dark:#555;
  --brand:#3b6fae;
  --rule:#9a9a9a;
  --table-head:#b3b3b3;
  --pastel-gradient:linear-gradient(90deg,#f3b37d,#e7a0ae,#9fb7d9,#b7cf7b,#b9a4cf,#8fbfe0,#f3b37d);
  --card-red:linear-gradient(135deg,#a8163a,#d8265a);
  --card-orange:linear-gradient(135deg,#f18a1c,#f6a12a);
  --card-green:linear-gradient(135deg,#7fbe3a,#d7e22a);
  --card-purple:linear-gradient(135deg,#6a3f8f,#9a6fb3);
  --card-blue:linear-gradient(135deg,#1a5fa6,#1aa3d8);
}
*{margin:0;padding:0;box-sizing:border-box}
html,body{width:1200px;height:1000px;overflow:hidden;background:var(--stage)}
body{position:relative;font-family:"Open Sans",Arial,sans-serif;color:var(--ink)}
.sheet{position:absolute;background:var(--paper);box-shadow:0 1px 3px rgba(0,0,0,.18);overflow:hidden}
.pattern{position:absolute;background:var(--pastel-gradient)}
.pattern--faint{opacity:.22}
.pattern--full{opacity:.55}

/* letterhead */
.letterhead{left:47px;top:141px;width:356px;height:504px}
.letterhead .pattern--top{left:50px;top:0;width:262px;height:17px}
.letterhead .pattern--bottom{left:50px;top:458px;width:262px;height:46px}
.sender{position:absolute;font-size:6.5px;font-weight:600;line-height:9px;font-style:normal;color:var(--ink)}
.letterhead .sender{left:43px;top:70px}
.letter-body{position:absolute;left:43px;top:131px;width:266px;font-size:6.6px;font-weight:600;line-height:12.6px;text-align:justify;color:var(--ink)}
.letter-body p{margin-bottom:12.6px}
.letter-body p.run-on{margin-bottom:0}
.letter-body .salutation{margin-bottom:12px}
.signature{display:block;margin-top:2px}

/* invoice */
.invoice{left:425px;top:141px;width:355px;height:504px}
.invoice .sender{left:48px;top:43px}
.brand{position:absolute;display:flex;align-items:center;gap:4px;color:var(--brand);font-weight:700;text-transform:uppercase;line-height:1}
.brand__dot{width:12px;height:12px;border-radius:50%;background:var(--brand);flex:none}
.invoice .brand{left:226px;top:45px;font-size:7px}
.field{position:absolute;font-size:7px;display:flex;align-items:flex-end;gap:3px}
.field__line{display:inline-block;border-bottom:1px solid var(--rule);height:8px}
.invoice-table{position:absolute;left:48px;top:122px;width:262px;height:290px;border:1px solid var(--rule)}
.invoice-table__head{height:17px;background:var(--table-head);display:flex;justify-content:space-between;align-items:center;padding:0 20px 0 14px;font-size:8px;font-weight:600;color:#3f3f3f}
.invoice-table__total{position:absolute;left:0;right:0;bottom:0;height:16px;border-top:1px solid var(--rule);font-size:8px;padding-left:14px;line-height:15px}

/* a4 envelope */
.a4-flap{position:absolute;left:803px;top:88px;width:355px;height:54px}
.a4-envelope{left:803px;top:141px;width:355px;height:504px}

/* dl envelope */
.dl-envelope{left:47px;top:674px;width:356px;height:164px}
.dl-flap{position:absolute;left:47px;top:674px;width:356px;height:42px}
.dl-back{left:425px;top:674px;width:351px;height:164px}

/* business cards */
.card{position:absolute;width:153px;height:85px;box-shadow:0 1px 3px rgba(0,0,0,.25);color:#fff}
.card__name{position:absolute;left:18px;top:25px;font-size:8.5px;font-weight:600}
.card__details{position:absolute;left:64px;top:41px;font-size:5.6px;line-height:6.8px}
.card--front{left:803px;top:671px;background:#fafafa}
.card--front .brand{left:14px;top:32px;font-size:9px}
.card--front .brand__dot{width:16px;height:16px}
.card--blue{left:1006px;top:671px;width:152px;background:var(--card-blue)}
.card--blue .card__name{left:25px;top:25px}
.card--blue .card__details{left:70px}
.card--red{left:45px;top:864px;background:var(--card-red)}
.card--orange{left:250px;top:864px;background:var(--card-orange)}
.card--green{left:424px;top:864px;background:var(--card-green)}
.card--purple{left:628px;top:864px;background:var(--card-purple)}

/* email signature */
.email{left:803px;top:768px;width:355px;height:193px;background:#fff;font-family:Arial,sans-serif;color:#222}
.email__toolbar{height:13px;background:#eef1f5;border-bottom:1px solid #c9d1dc;font-size:5.5px;display:flex;align-items:center;gap:10px;padding-left:4px}
.email__row{display:flex;align-items:center;height:11px;font-size:5.5px;padding-left:8px;gap:10px}
.email__row input{all:unset;flex:1;height:8px;margin-right:6px;border:1px solid #c9d1dc;font-size:5px;padding-left:2px;line-height:8px}
.email__format{height:11px;background:#eef1f5;border-top:1px solid #c9d1dc;border-bottom:1px solid #c9d1dc;font-size:5.5px;display:flex;align-items:center;gap:8px;padding-left:4px;margin-top:2px}
.email__body{padding:10px 6px;font-size:7px;line-height:9px}
.email__body p{margin-bottom:6px}
.email__sig{margin-top:22px;font-size:6.5px;line-height:8px}
.email__sig .brand{position:static;font-size:7px;margin-top:2px}
</style>
</head>
<body>

<!-- Letterhead -->
<section class="sheet letterhead">
  <div class="pattern pattern--faint pattern--top" role="img" aria-label="Faint band of pastel brand lettering"></div>
  <address class="sender">Brightpath<br>12 Larch Road<br>2260 Kelmore</address>
  <div class="letter-body">
    <p class="salutation">Dear Mrs Reed</p>
    <p class="run-on">Lorem ipsum dolor sit amet, consectetur adipisicing elit, sed do eiusmod tempor incididunt ut labore et dolore magna aliqua. Ut enim ad minim veniam, quis nostrud exercitation ullamco laboris nisi ut aliquip ex ea commodo consequat. Duis aute irure dolor in reprehenderit in voluptate velit esse cillum dolore eu fugiat nulla pariatur. Excepteur sint occaecat cupidatat non proident, sunt in culpa qui officia deserunt mollit anim id est laborum.</p>
    <p>Lorem ipsum dolor sit amet, consectetur adipisicing elit, sed do eiusmod tempor incididunt ut labore et dolore magna aliqua. Ut enim ad minim veniam, quis nostrud exercitation ullamco laboris nisi ut aliquip ex ea commodo consequat.</p>
    <p>Lorem ipsum dolor sit amet, consectetur adipisicing elit, sed do eiusmod tempor incididunt ut labore et dolore magna aliqua. Ut enim ad minim veniam, quis nostrud exercitation ullamco laboris nisi ut aliquip ex ea commodo consequat.</p>
    <p style="margin-bottom:4px">Sincerely,</p>
    <svg class="signature" width="70" height="36" viewBox="0 0 70 36" aria-label="Signature" role="img"><path d="M10 30 C4 20 12 6 16 10 C20 14 8 32 14 30 C20 28 22 16 26 20 C30 24 40 18 66 16" fill="none" stroke="#444" stroke-width="0.8"/></svg>
  </div>
  <div class="pattern pattern--faint pattern--bottom" role="img" aria-label="Faint band of pastel brand lettering"></div>
</section>

<!-- Invoice / quotation -->
<section class="sheet invoice">
  <address class="sender">Brightpath<br>12 Larch Road<br>2260 Kelmore</address>
  <div class="brand"><span class="brand__dot"></span><span>Brightpath<br>Disability Services</span></div>
  <div class="field" style="left:48px;top:97px;font-size:6px">Supplier <span class="field__line" style="width:58px"></span></div>
  <div class="field" style="left:211px;top:99px">Supplier <span class="field__line" style="width:66px"></span></div>
  <div class="invoice-table">
    <div class="invoice-table__head"><span>Item</span><span>Amount</span></div>
    <div class="invoice-table__total">Total</div>
  </div>
  <div class="field" style="left:50px;top:433px;font-size:8px">Supplier <span class="field__line" style="width:72px"></span></div>
</section>

<!-- A4 envelope -->
<svg class="a4-flap" viewBox="0 0 355 54" role="img" aria-label="Envelope flap">
  <defs><linearGradient id="flapGreen" x1="0" x2="1"><stop offset="0" stop-color="#8cc63f"/><stop offset="1" stop-color="#d9e021"/></linearGradient></defs>
  <polygon points="0,54 28,3 327,3 355,54" fill="url(#flapGreen)"/>
  <polygon points="28,3 327,3 325,0 30,0" fill="#c8c8c8"/>
</svg>
<section class="sheet a4-envelope">
  <div class="pattern pattern--full" style="inset:0" role="img" aria-label="All-over pattern of repeated pastel brand lettering"></div>
</section>

<!-- DL envelope -->
<section class="sheet dl-envelope"></section>
<svg class="dl-flap" viewBox="0 0 356 42" role="img" aria-label="Envelope flap lined with pastel brand pattern">
  <defs><linearGradient id="flapPastel" x1="0" x2="1">
    <stop offset="0" stop-color="#f3b37d"/><stop offset=".25" stop-color="#e7a0ae"/><stop offset=".5" stop-color="#9fb7d9"/><stop offset=".75" stop-color="#b7cf7b"/><stop offset="1" stop-color="#b9a4cf"/>
  </linearGradient></defs>
  <polygon points="0,0 356,0 356,3 318,40 38,40 0,3" fill="url(#flapPastel)" opacity=".6"/>
</svg>
<section class="sheet dl-back">
  <div class="pattern pattern--full" style="inset:0" role="img" aria-label="All-over pattern of repeated pastel brand lettering"></div>
</section>

<!-- Business cards -->
<div class="card card--front"><div class="brand"><span class="brand__dot"></span><span>Brightpath<br>Disability Services</span></div></div>
<div class="card card--blue"><div class="card__name">Jordan Hale</div><div class="card__details">5184062<br>jordanhale@mail.example<br>www.jordanhale.example</div></div>
<div class="card card--red"><div class="card__name">Jordan Hale</div><div class="card__details">5184062<br>jordanhale@mail.example<br>www.jordanhale.example</div></div>
<div class="card card--orange"><div class="card__name">Jordan Hale</div><div class="card__details">5184062<br>jordanhale@mail.example<br>www.jordanhale.example</div></div>
<div class="card card--green"><div class="card__name">Jordan Hale</div><div class="card__details">5184062<br>jordanhale@mail.example<br>www.jordanhale.example</div></div>
<div class="card card--purple"><div class="card__name">Jordan Hale</div><div class="card__details">5184062<br>jordanhale@mail.example<br>www.jordanhale.example</div></div>

<!-- Email signature -->
<section class="sheet email">
  <div class="email__toolbar"><span>Send</span><span>Options...</span><span>HTML</span></div>
  <div class="email__row" style="margin-top:3px"><span>To...</span><input value="sam"></div>
  <div class="email__row"><span>Cc...</span><input value="Sam Reed [sam@northfield.example]"></div>
  <div class="email__row"><span>Subject:</span><input value="Next Week"></div>
  <div class="email__format"><span>Arial</span><span>12</span><b>B</b><i>I</i><u>U</u></div>
  <div class="email__body">
    <p>Hi Sam,</p>
    <p>Back to school already! Do you have time to go through the ICT plan today?</p>
    <p>Thanks,</p>
    <div class="email__sig">Mia<br>12 Larch Road<br>2260 Kelmore
      <div class="brand"><span class="brand__dot" style="width:9px;height:9px"></span><span>Brightpath Disability Services</span></div>
    </div>
  </div>
</section>

</body>
</html>
```